verdant harbour requires some business cards

I need some business cards created that feature the company's newly designed logo. The business cards need to be be double sided and be a standard Australian size of 90mm x 55mm

Target Market(s)

business professionals, company executives, local goverment

Industry/Entity Type

Business

Requirements
Must have
• Company's logo
• The information section must include
• Individual name:
• Position:
• Phone:
• Address:
• Email:
• Website: www.verdantharbour.example
• The cards need to be easily formatted so I can enter staff members details positions etc...
• I plan to get these printed at deskmarket so can you please ensure that all designs meet their printing requirements http://www.deskmarket.example/retail/b2c/opsProductCreate.do?qty=1&cardQty=1000&sided=double&productname=colourbusinesscards&category=businesscards
Nice to have
• I might like to see some of the services we offer printed on one of the faces:
• Lighting Design (architectural, commercial, residential, theatrical ,exterior, interior) Lighting Consultancy, Theatrical Consultancy

```html
<!DOCTYPE html>
<html lang="en">
<head>
<meta charset="utf-8">
<title>verdant harbour — business cards</title>
<link rel="stylesheet" href="https://fonts.googleapis.com/css2?family=Arimo:wght@400&display=swap">
<style>
  :root {
    --backdrop: #5a5a5a;
    --card: #050505;
    --name-blue: #1ea3e6;
    --title-grey: #7d7d7d;
    --detail-grey: #a6a6a6;
    --logo-white: #ffffff;
    --band-teal: #1d6f9a;
    --band-blue: #2b3f9e;
    --band-violet: #6a3a9a;
    --band-magenta: #b03a6e;
    --band-red: #b8402a;
    --band-amber: #d08a1a;
  }
  * { margin: 0; padding: 0; box-sizing: border-box; }
  html, body {
    width: 1200px; height: 988px; overflow: hidden;
    background: var(--backdrop);
    font-family: "Arimo", Arial, sans-serif;
  }
  .card {
    position: absolute;
    width: 550px; height: 333px;
    background: var(--card);
    overflow: hidden;
  }
  .card--front { left: 138px; top: 115px; }
  .card--back  { left: 504px; top: 520px; }

  .light-band {
    position: absolute; inset: 0;
    background: linear-gradient(100deg, var(--band-teal) 0%, var(--band-blue) 25%, var(--band-violet) 45%, var(--band-magenta) 58%, var(--band-red) 75%, var(--band-amber) 100%);
    -webkit-mask-image: linear-gradient(to bottom, rgba(0,0,0,0.15) 0%, rgba(0,0,0,0.9) 45%, rgba(0,0,0,0.2) 70%, rgba(0,0,0,0) 92%);
            mask-image: linear-gradient(to bottom, rgba(0,0,0,0.15) 0%, rgba(0,0,0,0.9) 45%, rgba(0,0,0,0.2) 70%, rgba(0,0,0,0) 92%);
  }
  .card--back .light-band { opacity: 0.4; }

  .brand {
    position: absolute; left: 302px; top: 280px;
    display: flex; align-items: center; gap: 8px;
    color: var(--logo-white);
    font-size: 21px; letter-spacing: 0.2px;
  }
  .brand__dot {
    width: 14px; height: 14px; border-radius: 50%;
    background: var(--logo-white);
  }

  .person {
    position: absolute; right: 34px; top: 26px; text-align: right;
  }
  .person__name { color: var(--name-blue); font-size: 30px; line-height: 1.2; }
  .person__role { color: var(--title-grey); font-size: 14px; margin-top: 11px; }

  .contact {
    position: absolute; left: 32px; top: 210px;
    list-style: none;
    color: var(--detail-grey); font-size: 14.5px; line-height: 26px;
  }
</style>
</head>
<body>
  <section class="card card--front">
    <div class="light-band" role="img" aria-label="Dotted light pattern sweeping from teal and blue through violet to red and amber"></div>
    <div class="brand"><span class="brand__dot"></span><span class="brand__name">verdant harbour</span></div>
  </section>

  <section class="card card--back">
    <div class="light-band" role="img" aria-label="Faint dotted light pattern sweeping from blue to amber"></div>
    <div class="person">
      <p class="person__name">Marcus Ellery</p>
      <p class="person__role">Marketing director</p>
    </div>
    <ul class="contact">
      <li>+61 8 9000 4127</li>
      <li>www.verdantharbour.example</li>
      <li>marcus@verdantharbour.example</li>
      <li>PO Box 482, Perth WA 6000 Australia</li>
    </ul>
  </section>
</body>
</html>
```